Banner Design Project – Commercial & Residential Pest Control

The large 4' x 6' banner should attract commercial customers and emphasize our expertise in bed bug control, risk management, and commercial pest management.

The 3–4 smaller residential banners should work together to showcase the range of pest control services we offer homeowners, including general pest control, gopher and vole control, and mouse control.

Across the entire set, we want customers to understand that they are dealing with an experienced, professional, locally owned and operated family business that has been serving the community since 2017.

Details are in attached PDF. I also included pictures of our new trade show backdrop and current pictures of the area we are working in the banners will be on either wall NOT the back. The tables will remain. I have included a lot of our information and pictures to get an idea of the company.

```html
<!DOCTYPE html>
<html lang="en">
<head>
<meta charset="utf-8">
<title>Kestrel Pest Control – Commercial Banner</title>
<link rel="stylesheet" href="https://fonts.googleapis.com/css2?family=Bebas+Neue&family=Fira+Sans+Extra+Condensed:wght@600;700;800&display=swap">
<style>
  :root {
    --orange: #f4511e;
    --charcoal: #2d2d2d;
    --ink: #1f1f1f;
    --white: #ffffff;
  }
  * { margin: 0; padding: 0; box-sizing: border-box; }
  html, body { width: 1200px; height: 800px; overflow: hidden; background: var(--white); }
  .banner { position: relative; width: 1200px; height: 800px; background: var(--white); overflow: hidden; }

  .photo { position: absolute; inset: 0; width: 1200px; height: 800px; }

  .brand {
    position: absolute; left: 50px; top: 48px;
    display: flex; align-items: center; gap: 14px;
    font-family: "Fira Sans Extra Condensed", sans-serif;
    font-weight: 700; font-size: 58px; line-height: 1;
    color: var(--charcoal);
  }
  .brand-mark { width: 30px; height: 30px; background: var(--orange); }

  .headline {
    position: absolute; left: 46px; top: 170px;
    font-family: "Bebas Neue", sans-serif;
    font-weight: 400; font-size: 167px; line-height: 0.78; letter-spacing: 1px;
  }
  .headline .dark { color: var(--charcoal); display: block; }
  .headline .accent { color: var(--orange); display: block; }

  .tagline {
    position: absolute; left: 48px; top: 458px;
    font-family: "Fira Sans Extra Condensed", sans-serif;
    font-weight: 800; font-size: 47px; line-height: 1.0;
    color: var(--ink); text-transform: uppercase; letter-spacing: 1.2px;
  }
  .tagline em { font-style: normal; color: var(--orange); }

  .services {
    position: absolute; left: 50px; top: 576px;
    display: grid; grid-template-columns: 386px 420px; row-gap: 11px;
    list-style: none;
    font-family: "Fira Sans Extra Condensed", sans-serif;
    font-weight: 600; font-size: 22px; color: var(--charcoal);
  }
  .services li { display: flex; align-items: center; gap: 16px; height: 33px; white-space: nowrap; }
  .services li:nth-child(1) { grid-column: 1; grid-row: 1; }
  .services li:nth-child(2) { grid-column: 1; grid-row: 2; }
  .services li:nth-child(3) { grid-column: 1; grid-row: 3; }
  .services li:nth-child(4) { grid-column: 2; grid-row: 1; }
  .services li:nth-child(5) { grid-column: 2; grid-row: 2; }
  .shield { width: 32px; height: 36px; flex: none; }

  .footer-band {
    position: absolute; left: 0; top: 717px; width: 1200px; height: 83px;
    background: var(--charcoal);
    font-family: "Bebas Neue", sans-serif; font-size: 52px; line-height: 83px;
  }
  .footer-band svg { position: absolute; left: 0; top: 0; }
  .footer-local { position: absolute; left: 48px; top: 3px; color: var(--ink); }
  .footer-since { position: absolute; left: 558px; top: 3px; color: var(--white); letter-spacing: 0.5px; }
</style>
</head>
<body>
<div class="banner">

  <svg class="photo" viewBox="0 0 1200 800" role="img" aria-label="Photo of a pest control technician kneeling on a lawn beside a house, using a hand sprayer">
    <defs>
      <linearGradient id="sceneTone" x1="0" y1="0" x2="0" y2="1">
        <stop offset="0" stop-color="#e6e2da"/>
        <stop offset="0.32" stop-color="#d2cdc3"/>
        <stop offset="0.48" stop-color="#8fa65a"/>
        <stop offset="1" stop-color="#6a8a36"/>
      </linearGradient>
      <linearGradient id="edgeFade" gradientUnits="userSpaceOnUse" x1="690" y1="717" x2="930" y2="470">
        <stop offset="0" stop-color="#ffffff"/>
        <stop offset="0.35" stop-color="#ffffff" stop-opacity="0.75"/>
        <stop offset="1" stop-color="#ffffff" stop-opacity="0"/>
      </linearGradient>
      <clipPath id="photoShape">
        <polygon points="724,0 1200,0 1200,717 690,717 842,253"/>
      </clipPath>
    </defs>
    <g clip-path="url(#photoShape)">
      <rect x="680" y="0" width="520" height="717" fill="url(#sceneTone)"/>
      <rect x="680" y="0" width="520" height="717" fill="url(#edgeFade)"/>
    </g>
  </svg>

  <div class="brand"><span class="brand-mark"></span>Kestrel Pest Control</div>

  <h1 class="headline">
    <span class="dark">Commercial</span>
    <span class="accent">Expertise</span>
  </h1>

  <p class="tagline">
    Protecting your <em>business.</em><br>
    Managing your <em>risk.</em>
  </p>

  <ul class="services">
    <li><svg class="shield" viewBox="0 0 32 36"><path d="M16 1 L30 6 V17 C30 26 23 32 16 35 C9 32 2 26 2 17 V6 Z" fill="#f4511e"/><path d="M16 5 L26 8.5 V17 C26 24 21 28.5 16 31 C11 28.5 6 24 6 17 V8.5 Z" fill="#2d2d2d"/><path d="M10.5 18 L14.5 22 L22 13.5" fill="none" stroke="#fff" stroke-width="2.6" stroke-linecap="round" stroke-linejoin="round"/></svg>Bed Bug Control &amp; Risk Management</li>
    <li><svg class="shield" viewBox="0 0 32 36"><path d="M16 1 L30 6 V17 C30 26 23 32 16 35 C9 32 2 26 2 17 V6 Z" fill="#f4511e"/><path d="M16 5 L26 8.5 V17 C26 24 21 28.5 16 31 C11 28.5 6 24 6 17 V8.5 Z" fill="#2d2d2d"/><path d="M10.5 18 L14.5 22 L22 13.5" fill="none" stroke="#fff" stroke-width="2.6" stroke-linecap="round" stroke-linejoin="round"/></svg>General Commercial Pest Control</li>
    <li><svg class="shield" viewBox="0 0 32 36"><path d="M16 1 L30 6 V17 C30 26 23 32 16 35 C9 32 2 26 2 17 V6 Z" fill="#f4511e"/><path d="M16 5 L26 8.5 V17 C26 24 21 28.5 16 31 C11 28.5 6 24 6 17 V8.5 Z" fill="#2d2d2d"/><path d="M10.5 18 L14.5 22 L22 13.5" fill="none" stroke="#fff" stroke-width="2.6" stroke-linecap="round" stroke-linejoin="round"/></svg>Rodent Control</li>
    <li><svg class="shield" viewBox="0 0 32 36"><path d="M16 1 L30 6 V17 C30 26 23 32 16 35 C9 32 2 26 2 17 V6 Z" fill="#f4511e"/><path d="M16 5 L26 8.5 V17 C26 24 21 28.5 16 31 C11 28.5 6 24 6 17 V8.5 Z" fill="#2d2d2d"/><path d="M10.5 18 L14.5 22 L22 13.5" fill="none" stroke="#fff" stroke-width="2.6" stroke-linecap="round" stroke-linejoin="round"/></svg>Fly Management &amp; Maintenance</li>
    <li><svg class="shield" viewBox="0 0 32 36"><path d="M16 1 L30 6 V17 C30 26 23 32 16 35 C9 32 2 26 2 17 V6 Z" fill="#f4511e"/><path d="M16 5 L26 8.5 V17 C26 24 21 28.5 16 31 C11 28.5 6 24 6 17 V8.5 Z" fill="#2d2d2d"/><path d="M10.5 18 L14.5 22 L22 13.5" fill="none" stroke="#fff" stroke-width="2.6" stroke-linecap="round" stroke-linejoin="round"/></svg>Ongoing preventative pest management</li>
  </ul>

  <div class="footer-band">
    <svg width="560" height="83" viewBox="0 0 560 83"><polygon points="0,0 518,0 536,41.5 518,83 0,83" fill="#f4511e"/></svg>
    <span class="footer-local">Locally Owned &amp; Operated</span>
    <span class="footer-since">Serving Our Community Since 2017</span>
  </div>

</div>
</body>
</html>
```